Biz technology consulting firm like a global company (better than Corvellant, etc)

Check word document high level requirements, a_design_webpage_content attached providing more details for content and message to convey to potential customers..  Create a crisp, clear and engaging business consulting website design that allows the user to understand the value that Brimquora can deliver to their company.  We focus on innovation, simplification, creative solutions, digital transformations ERP, CRM, Analytics, project management, making IT simple and coaching enterprises how to align and implement technologies to support business strategy and goals. Whether a startup or a global billion dollar firm, we increase EBITDA through innovation and digital transformation.  

I desire to have sections that highlight each of the core areas such as: (**Please see  brimquora.example and the design word document that is attached below for core areas of focus**)

Feel free to go to Brimquora.example and review the basic categories to understand at a very high level the categories that are key.

Help me create a brand and website that engages startups, Private Equity firms seeking carve-out, integration experience and large corporate enterprises searching to convert to data driven and customer focused enterprises.  
Hero section with a tagline that emphasizes the company's focus on Tilting the view.  We help you visualize outcomes with a positive and collaborative solution driven mindset.  When you look at life through a different "positive" lens, you can convert all problems to opportunities.  Align your IT team with your business goals and you quickly realize the value of all processes and technology deployed in your enterprise; increasing EBITDA, morale, and long term success.

We evaluate your current state, create a custom roadmap for alignment, coach  and empower you to lead while removing the uncertainty and silos.  Partner with the experts who help make business and technology simple and effective
Call-to-action section encouraging visitors to learn more about the company's services and expertise
Services -- detail provided in the attached word document (please use)
Section providing an overview of the company's services, including digital transformation, strategy, change management, CRM, ERP, automation, AI, data / analytics, process optimization, carve-outs, integrations, scaling, risk mitigation, security and marketing.
Call-to-action section encouraging visitors to learn more about the company's expertise and how it can help their business and encouraging visitors to schedule a consultation or assessment.
Footer
Navigation menu
Contact information
LinkedIn link
The website should have a modern and professional design, with a focus on clear messaging and easy navigation. The color scheme will be clean and simple, with a mix of colors to convey trust, reliability, and innovation. The website will be optimized for search engines and mobile devices, ensuring that visitors can easily access the site from any device.

Companies who desire to grow their business, optimize their processes, maximize the output of human capital and profitablity.

Business Technology consulting

• designer should choose for professional audience

• easy navigation, engaging flow, professional layout and colors that represent confidence, excellence and innovation in a world full of change.
• I would like to see you blend in the play on PIVOT's (changes that we face in business and life), the different way we may look at things and the unique way we solve problems. All of these are options to Tilt the view and leverage the unique views of individuals, millions of data points, workflow and technology enablers to deliver maximize value to your enterprise

```html
<!DOCTYPE html>
<html lang="en">
<head>
<meta charset="utf-8">
<title>Brimquora — Tilt the view</title>
<link href="https://fonts.googleapis.com/css2?family=League+Spartan:wght@500;600;700;800&family=Kumbh+Sans:wght@400;500;600;700&display=swap" rel="stylesheet">
<style>
:root{
  --blue:#1b3fc6;
  --blue-deep:#0d2a9e;
  --blue-dark:#0a1f7a;
  --heading:#1d3fbf;
  --link:#2a4fd6;
  --orange:#f07a1a;
  --hero-bg:#eaf1fd;
  --ink:#1c1c28;
  --text:#3a3a48;
  --white:#ffffff;
  --card-shadow:0 6px 22px rgba(30,60,160,.12);
}
*{box-sizing:border-box;margin:0;padding:0}
html,body{width:1200px;height:3696px;overflow:hidden}
body{position:relative;background:var(--white);font-family:"Kumbh Sans",sans-serif;color:var(--ink)}
.abs{position:absolute}
h1,h2,h3,.brand{font-family:"League Spartan",sans-serif}

/* header */
.site-header{position:absolute;left:0;top:0;width:1200px;height:82px;background:var(--white);border-bottom:1px solid #e6ebf5}
.brand{position:absolute;color:var(--link);font-weight:800;letter-spacing:.5px}
.site-header .brand{left:86px;top:24px;font-size:31px}
.main-nav{position:absolute;right:85px;top:31px;display:flex;gap:22px;font-size:15px;font-weight:500;color:var(--ink)}

/* hero */
.hero{position:absolute;left:0;top:82px;width:1200px;height:581px;background:var(--hero-bg);overflow:hidden}
.hero-wave{position:absolute;left:0;bottom:0}
.hero .eyebrow{position:absolute;left:86px;top:96px;font-size:26px;color:var(--heading);font-weight:500}
.hero h1{position:absolute;left:84px;top:138px;font-size:62px;font-weight:800;color:var(--heading);letter-spacing:.5px}
.hero p{position:absolute;left:86px;top:220px;width:460px;font-size:15.5px;line-height:24px;color:var(--text)}
.btn-more{position:absolute;left:87px;top:343px;width:145px;height:40px;border-radius:20px;background:var(--orange);color:var(--white);font-size:14px;font-weight:600;display:flex;align-items:center;padding-left:16px}
.btn-more svg{position:absolute;right:7px;top:7px}
.hero-blob{position:absolute;left:600px;top:30px;width:520px;height:470px;border-radius:50% 46% 42% 50%;background:#d3e0fb}
.hero-art{position:absolute;left:640px;top:60px;width:470px;height:470px;border-radius:22px;background:linear-gradient(160deg,#3d5fe0,#1d3fbf 55%,#a9c1f6)}

/* about */
.about{position:absolute;left:0;top:663px;width:1200px;height:344px;background:var(--blue)}
.about-art{position:absolute;left:54px;top:44px;width:560px;height:256px;border-radius:16px;background:linear-gradient(135deg,#2f56d8,#5a80ee 55%,#2549cc)}
.about h2{position:absolute;left:662px;top:84px;font-size:37px;color:var(--white);font-weight:700}
.about p{position:absolute;left:662px;top:140px;width:462px;font-size:16px;line-height:24.5px;color:var(--white)}

/* section titles */
.section-title{position:absolute;left:0;width:1200px;text-align:center;font-size:35px;font-weight:700;color:var(--heading)}

/* services */
.service-card{position:absolute;top:1138px;width:330px;height:444px;background:var(--white);border-radius:16px;box-shadow:var(--card-shadow)}
.service-art{position:absolute;left:35px;top:28px;width:260px;height:210px;border-radius:14px;background:linear-gradient(160deg,#e4ecfd,#9fb7f3)}
.service-card h3{position:absolute;left:30px;top:278px;width:270px;text-align:center;font-size:27px;line-height:32px;font-weight:600;color:var(--heading)}
.dots{position:absolute;left:0;width:1200px;display:flex;justify-content:center;gap:14px}
.dots span{width:11px;height:11px;border-radius:50%;border:2px solid var(--link)}
.dots span.on{background:var(--link)}
.dots.light span{border-color:var(--white)}
.dots.light span.on{background:var(--white)}

/* core offerings */
.offering{position:absolute;width:500px;height:110px}
.offering .icon{position:absolute;left:0;top:0;width:86px;height:86px;border-radius:50%;background:radial-gradient(circle at 35% 30%,#2c56e0,#102e9e)}
.offering .icon svg{position:absolute;left:21px;top:21px}
.offering h3{position:absolute;left:102px;top:-1px;font-family:"Kumbh Sans",sans-serif;font-size:15px;font-weight:600;color:var(--link)}
.offering p{position:absolute;left:102px;top:18px;width:395px;font-size:12.6px;line-height:18px;color:var(--text);text-align:justify}

/* why */
.why{position:absolute;left:0;top:2309px;width:1200px;height:475px;background:linear-gradient(90deg,#1841cf,#0f2fae 70%,#0a1f7a)}
.why h2{position:absolute;left:0;top:42px;width:1200px;text-align:center;font-size:37px;font-weight:700;color:var(--white)}
.why-card{position:absolute;width:196px;height:259px;background:var(--white);border-radius:10px;text-align:center;padding:0 16px}
.why-card svg{display:block;margin:18px auto 10px}
.why-card h3{font-family:"Kumbh Sans",sans-serif;font-size:13px;line-height:17px;font-weight:600;color:var(--link);margin-bottom:12px}
.why-card p{font-size:10.4px;line-height:14px;color:var(--text)}

/* contact */
.touch-intro{position:absolute;left:0;top:2885px;width:1200px;text-align:center;font-size:14px;line-height:22px;color:var(--ink)}
.touch-art{position:absolute;left:86px;top:2935px;width:1028px;height:265px;border-radius:130px;background:linear-gradient(90deg,#2c4fd4,#c9d6fa 28%,#f3f6fe 50%,#c9d6fa 72%,#2c4fd4)}
.brand-footer{left:0;top:3226px;width:1200px;text-align:center;font-size:52px;color:var(--blue)}
.contact-card{position:absolute;top:3315px;width:310px;height:215px;background:var(--white);box-shadow:var(--card-shadow);text-align:center}
.contact-card .c-icon{position:absolute;left:116px;top:28px;width:78px;height:78px;border-radius:50%;background:var(--orange)}
.contact-card .c-icon svg{position:absolute;left:19px;top:19px}
.contact-card h3{position:absolute;left:0;top:124px;width:310px;font-family:"Kumbh Sans",sans-serif;font-size:20px;font-weight:600;color:var(--link)}
.contact-card p{position:absolute;left:0;top:156px;width:310px;font-size:16px;line-height:21px;color:var(--ink)}
.social{position:absolute;left:460px;top:3571px;display:flex;gap:16px}
.social a{display:block;width:43px;height:43px;border-radius:50%;background:var(--orange)}
.copyright{position:absolute;left:0;top:3640px;width:1200px;text-align:center;font-size:15px;letter-spacing:1.6px;color:var(--ink)}
</style>
</head>
<body>

<header class="site-header">
  <div class="brand">BRIMQUORA</div>
  <nav class="main-nav">
    <span>Home</span><span>About Brimquora</span><span>Our Services</span><span>Core Offerings</span><span>Why Us</span><span>Contact Us</span>
  </nav>
</header>

<section class="hero">
  <svg class="hero-wave" width="1200" height="200" viewBox="0 0 1200 200"><path d="M0 60 C120 10 240 40 330 90 C420 140 500 170 540 200 L0 200Z" fill="#d6e3fb"/></svg>
  <div class="hero-blob"></div>
  <div class="hero-art" role="img" aria-label="Illustration of two people reviewing a large dashboard of charts"></div>
  <div class="eyebrow">Welcome to Brimquora</div>
  <h1>TILT THE VIEW</h1>
  <p>Every business is unique. That's why we take a personalized approach to every project, working closely with you to understand your goals and create tailored solutions that work for you.</p>
  <a class="btn-more">Read More
    <svg width="26" height="26" viewBox="0 0 26 26"><circle cx="13" cy="13" r="12" fill="#fff"/><path d="M8 13h9M13 9l4 4-4 4" stroke="#f07a1a" stroke-width="2.2" fill="none" stroke-linecap="round" stroke-linejoin="round"/></svg>
  </a>
</section>

<section class="about">
  <div class="about-art" role="img" aria-label="Illustration of a team at laptops with a presenter beside a strategy board"></div>
  <h2>About Brimquora</h2>
  <p>At Brimquora, we specialize in driving transformative change and innovation to help businesses thrive in today's dynamic landscape. Our comprehensive suite of services is designed to elevate your organization's performance, streamline operations, and foster sustainable growth.</p>
</section>

<h2 class="section-title" style="top:1052px">Our Services</h2>
<article class="service-card" style="left:86px">
  <div class="service-art" role="img" aria-label="Illustration of SaaS cloud servers connected to workstations"></div>
  <h3>SaaS CRM (Loyalty &amp; Subscription) Apps / Segmentation / Rewards</h3>
</article>
<article class="service-card" style="left:435px">
  <div class="service-art" role="img" aria-label="Illustration of people assembling puzzle pieces on a laptop"></div>
  <h3>Strategy / Org Design / Competitive Analysis / Change Management</h3>
</article>
<article class="service-card" style="left:784px">
  <div class="service-art" role="img" aria-label="Illustration of people working around a globe"></div>
  <h3>M&amp;A - (Carve-outs / Integrations) Diligence / TSA / IMO / Interim CxO</h3>
</article>
<div class="dots" style="top:1611px"><span class="on"></span><span></span><span></span></div>

<h2 class="section-title" style="top:1691px">Core Offerings</h2>

<div class="offering" style="left:86px;top:1782px"><div class="icon"><svg width="44" height="44" viewBox="0 0 44 44" fill="none" stroke="#fff" stroke-width="2.6" stroke-linecap="round"><rect x="9" y="7" width="26" height="32" rx="3"/><rect x="16" y="4" width="12" height="6" rx="2" fill="#fff"/><path d="M15 18l4 4M19 18l-4 4M25 28l4 4M29 28l-4 4M17 32c3-6 8-8 10-13"/></svg></div><h3>Strategy</h3><p>Our strategic consulting services are tailored to align your business objectives with actionable technology initiatives, enabling you to navigate challenges, seize opportunities and achieve your business goals with confidence.</p></div>
<div class="offering" style="left:618px;top:1782px"><div class="icon"><svg width="44" height="44" viewBox="0 0 44 44" fill="none" stroke="#fff" stroke-width="2.6" stroke-linecap="round"><circle cx="22" cy="22" r="17" stroke-dasharray="6 3"/><circle cx="22" cy="22" r="11"/><path d="M17 26v-3M22 26v-7M27 26v-10"/></svg></div><h3>Process Optimization</h3><p>We specialize in optimizing processes to enhance efficiency, reduce costs, and drive operational excellence, ensuring that your business operates at its full potential.</p></div>
<div class="offering" style="left:86px;top:1910px"><div class="icon"><svg width="44" height="44" viewBox="0 0 44 44" fill="none" stroke="#fff" stroke-width="2.6" stroke-linecap="round" stroke-linejoin="round"><circle cx="22" cy="14" r="9" stroke-dasharray="5 3"/><path d="M6 28l8-5 6 3 6-3 6 3 6 5M12 32l6 5M18 29l7 7M24 27l7 7"/></svg></div><h3>CRM, loyalty, rewards, and Customer Experience</h3><p>Elevate your customer engagement and loyalty with our CRM solutions, designed to deliver exceptional customer experiences and foster lasting relationships.</p></div>
<div class="offering" style="left:618px;top:1910px"><div class="icon"><svg width="44" height="44" viewBox="0 0 44 44" fill="none" stroke="#fff" stroke-width="2.6" stroke-linecap="round"><path d="M22 8a10 10 0 0 0-6 18v5h12v-5a10 10 0 0 0-6-18z"/><path d="M18 36h8M22 4v-2M8 18H5M39 18h-3M11 8l-2-2M33 8l2-2"/></svg></div><h3>Innovation and Application Design</h3><p>Embrace innovation with our cutting-edge application design and development services, tailored to meet your unique business needs and drive digital transformation.</p></div>
<div class="offering" style="left:86px;top:2038px"><div class="icon"><svg width="44" height="44" viewBox="0 0 44 44" fill="none" stroke="#fff" stroke-width="2.6" stroke-linecap="round"><circle cx="18" cy="18" r="12"/><path d="M12 15h12M12 20h9M27 27l11 11"/></svg></div><h3>Interim CxO and Private Equity Diligence</h3><p>Our seasoned professionals provide interim CxO support and comprehensive private equity diligence services to guide your business through critical transitions and investment decisions.</p></div>
<div class="offering" style="left:618px;top:2038px"><div class="icon"><svg width="44" height="44" viewBox="0 0 44 44" fill="#fff"><rect x="5" y="6" width="15" height="15" rx="2"/><rect x="24" y="6" width="15" height="15" rx="2" opacity=".75"/><rect x="5" y="25" width="15" height="15" rx="2" opacity=".75"/><circle cx="31" cy="32" r="7" fill="none" stroke="#fff" stroke-width="2.6"/></svg></div><h3>Carve-outs and Integrations</h3><p>Navigate complex carve-out processes and seamless integrations with our expert guidance, ensuring a smooth transition and optimized operational integration.</p></div>
<div class="offering" style="left:86px;top:2165px"><div class="icon"><svg width="44" height="44" viewBox="0 0 44 44" fill="none" stroke="#fff" stroke-width="2.6" stroke-linecap="round"><path d="M36 22a14 14 0 0 1-24 10M8 22a14 14 0 0 1 24-10"/><path d="M32 6v6h-6M12 38v-6h6"/><circle cx="22" cy="22" r="6"/></svg></div><h3>Change Management</h3><p>Embrace change with confidence. Our change management expertise empowers your organization to adapt, evolve, and thrive in the face of any transformational shift.</p></div>
<div class="offering" style="left:618px;top:2165px"><div class="icon"><svg width="44" height="44" viewBox="0 0 44 44" fill="none" stroke="#fff" stroke-width="2.6" stroke-linecap="round"><rect x="10" y="10" width="24" height="24" rx="3"/><path d="M16 4v6M22 4v6M28 4v6M16 34v6M22 34v6M28 34v6M4 16h6M4 28h6M34 16h6M34 28h6"/><text x="22" y="26" text-anchor="middle" font-family="Kumbh Sans, sans-serif" font-size="11" font-weight="700" fill="#fff" stroke="none">AI</text></svg></div><h3>AI and Analytics</h3><p>Leverage the power of AI and advanced analytics to gain actionable insights, drive informed decision-making, and unlock new opportunities for growth.</p></div>

<section class="why">
  <h2>Why partner with Brimquora</h2>
  <div class="why-card" style="left:86px;top:113px">
    <svg width="40" height="36" viewBox="0 0 40 36"><circle cx="29" cy="11" r="7" fill="none" stroke="#f07a1a" stroke-width="3"/><path d="M4 30h14l-8-10h12" stroke="#f07a1a" stroke-width="3" fill="none"/></svg>
    <h3>Enhanced IT<br>Roadmap Visibility</h3>
    <p>A digital transformation agency can improve IT roadmap visibility and awareness throughout the organization, ensuring that technology initiatives are aligned with business objectives and promoting collaboration among IT team members and other departments.</p>
  </div>
  <div class="why-card" style="left:294px;top:146px">
    <svg width="36" height="36" viewBox="0 0 36 36"><rect x="5" y="4" width="22" height="28" rx="3" fill="#f07a1a"/><path d="M10 12h12M10 18h8" stroke="#fff" stroke-width="2.4"/></svg>
    <h3>Improved Written<br>Communication</h3>
    <p>The agency can enhance written communication practices, facilitating effective information sharing and collaboration across the organization.</p>
  </div>
  <div class="why-card" style="left:502px;top:113px">
    <svg width="40" height="36" viewBox="0 0 40 36"><rect x="3" y="3" width="10" height="10" fill="#f07a1a"/><rect x="27" y="3" width="10" height="10" fill="#f07a1a"/><rect x="3" y="23" width="10" height="10" fill="#f07a1a"/><rect x="27" y="23" width="10" height="10" fill="#f07a1a"/><path d="M13 8h14M13 28h14M8 13v10M32 13v10" stroke="#f07a1a" stroke-width="2"/></svg>
    <h3>Cross-Functional Awareness<br>and Collaboration</h3>
    <p>By promoting cross-functional awareness of roles and responsibilities, the agency can foster collaboration and knowledge sharing among different departments, leading to a more cohesive and aligned organizational structure.</p>
  </div>
  <div class="why-card" style="left:710px;top:146px">
    <svg width="36" height="36" viewBox="0 0 36 36"><circle cx="18" cy="15" r="9" fill="#f07a1a"/><rect x="14" y="26" width="8" height="6" fill="#f07a1a"/></svg>
    <h3>Proactive<br>Problem-Solving</h3>
    <p>The agency can instill a culture of proactive problem-solving, addressing issues before they become critical and promoting a solution-driven and customer-centric service mentality.</p>
  </div>
  <div class="why-card" style="left:918px;top:113px">
    <svg width="40" height="36" viewBox="0 0 40 36"><rect x="4" y="4" width="32" height="22" rx="3" fill="#f07a1a"/><circle cx="14" cy="30" r="4" fill="#f07a1a"/><circle cx="26" cy="30" r="4" fill="#f07a1a"/></svg>
    <h3>Mentoring<br>and Coaching</h3>
    <p>Through active mentoring and coaching, the agency can help team members understand the value of their contributions in terms of security, compliance, standardization, scalability, and overall business impact.</p>
  </div>
  <div class="dots light" style="top:423px"><span class="on"></span><span></span><span></span></div>
</section>

<h2 class="section-title" style="top:2824px">Get In Touch</h2>
<p class="touch-intro">Ready to embark on a transformative journey? Contact us today to explore how our<br>comprehensive consulting services can elevate your business to new heights.</p>
<div class="touch-art" role="img" aria-label="Illustration of people untangling scribbled lines into an orderly spiral"></div>
<div class="brand abs brand-footer">BRIMQUORA</div>

<div class="contact-card" style="left:116px">
  <div class="c-icon"><svg width="40" height="40" viewBox="0 0 24 24"><path d="M6.6 10.8a15 15 0 0 0 6.6 6.6l2.2-2.2c.3-.3.7-.4 1-.2 1.1.4 2.3.6 3.6.6.6 0 1 .4 1 1V20c0 .6-.4 1-1 1A17 17 0 0 1 3 4c0-.6.4-1 1-1h3.5c.6 0 1 .4 1 1 0 1.3.2 2.5.6 3.6.1.3 0 .7-.2 1z" fill="#fff"/></svg></div>
  <h3>Phone Number</h3><p>+46 (0)700 00 12 34</p>
</div>
<div class="contact-card" style="left:443px">
  <div class="c-icon"><svg width="40" height="40" viewBox="0 0 24 24"><rect x="3" y="6" width="18" height="12" rx="1.5" fill="none" stroke="#fff" stroke-width="1.8"/><path d="M3.5 7l8.5 6 8.5-6" fill="none" stroke="#fff" stroke-width="1.8"/></svg></div>
  <h3>Email Address</h3><p>info@brimquora.example</p>
</div>
<div class="contact-card" style="left:772px">
  <div class="c-icon"><svg width="40" height="40" viewBox="0 0 24 24"><path d="M12 2a7 7 0 0 0-7 7c0 5.2 7 13 7 13s7-7.8 7-13a7 7 0 0 0-7-7z" fill="#fff"/><circle cx="12" cy="9" r="2.6" fill="#f07a1a"/></svg></div>
  <h3>Address</h3><p>P.O. Box 40210, Norvik,<br>Lanster 71830</p>
</div>

<nav class="social" aria-label="Social links">
  <a aria-label="Social link 1"></a><a aria-label="Social link 2"></a><a aria-label="Social link 3"></a><a aria-label="Social link 4"></a><a aria-label="Social link 5"></a>
</nav>
<p class="copyright">Copyright ©2023 Brimquora &nbsp;| &nbsp;Disclaimer, Terms &amp; Conditions</p>

</body>
</html>
```